" A VELMIRA é uma empresa de consultoria de Administraçao Contratual de Obras (destacadamente no segmento de infraestrutura e construçao pesada); Elaboraçao de pleitos/reivindicaçoes ("claim") para reequilíbrio econômico-financeiro de contratos de empreendimentos; Gerenciamento de Projetos; Gestao de Empreendimentos; Fiscalizaçao; Auditoria; Gestao Empresarial; Planejamento e Controle de Obras; Análise de Riscos de Empreendimentos; Orçamentos; Suporte para elaboraçao, análise e gestao de contratos. A sede da VELMIRA fica em Brasília/DF, entretanto a atuaçao ocorre em todo o Brasil conforme demanda dos clientes e localizaçao de suas obras. "

```html
<!DOCTYPE html>
<html lang="pt-BR">
<head>
<meta charset="utf-8">
<title>VELMIRA – Cartão de visita</title>
<link rel="stylesheet" href="https://fonts.googleapis.com/css2?family=Roboto:wght@400;500;700;900&display=swap">
<style>
  :root{
    --bg:#3a3a3c;
    --bg-dark:#262628;
    --blue-deep:#0f4a68;
    --blue-mid:#1a6d92;
    --blue-light:#3d9fc4;
    --blue-pale:#7cc4de;
    --white:#ffffff;
    --paper:#f4f6f7;
    --paper-shade:#d9dee1;
  }
  *{margin:0;padding:0;box-sizing:border-box}
  html,body{width:1200px;height:1200px;overflow:hidden}
  body{
    background:radial-gradient(circle at 50% 40%,var(--bg),var(--bg-dark));
    font-family:"Roboto",Arial,sans-serif;
    position:relative;
  }
  .card{
    position:absolute;left:120px;width:960px;height:533px;
    border-radius:4px;overflow:hidden;
    box-shadow:0 14px 40px rgba(0,0,0,.45);
  }
  /* Front */
  .card-front{
    top:50px;
    background:
      linear-gradient(125deg,rgba(255,255,255,.08) 0 30%,transparent 30% 52%,rgba(255,255,255,.05) 52% 68%,transparent 68%),
      radial-gradient(circle at 70% 35%,var(--blue-mid),var(--blue-deep) 75%);
    color:var(--white);
  }
  .front-bands{position:absolute;left:0;bottom:0;width:100%;height:80px}
  .brand{
    position:absolute;left:70px;top:110px;
    font-weight:900;font-size:78px;letter-spacing:2px;line-height:1;
  }
  .person{position:absolute;left:170px;top:205px;text-align:right;width:330px}
  .person-name{font-weight:700;font-size:24px;letter-spacing:1px}
  .person-role{font-size:22px;letter-spacing:14px;margin-top:4px;font-weight:500}
  .contacts{position:absolute;left:70px;top:290px;list-style:none}
  .contacts li{display:flex;align-items:center;gap:16px;font-size:20px;height:36px}
  .contacts .phones{font-weight:700;font-size:22px;margin-bottom:4px;padding-left:0}
  .contacts .icon{
    width:26px;height:26px;border-radius:3px;background:var(--blue-pale);
    display:flex;align-items:center;justify-content:center;flex:none;
  }
  .address{
    position:absolute;right:70px;top:240px;text-align:right;
    font-size:21px;line-height:1.35;
  }
  .address-label{font-weight:700;font-size:22px}
  .address-bar{
    position:absolute;right:60px;top:360px;width:260px;height:14px;
    background:var(--blue-pale);border-radius:2px;
  }
  /* Back */
  .card-back{
    top:633px;
    background:linear-gradient(160deg,var(--white) 0%,var(--paper) 55%,var(--paper-shade) 100%);
  }
  .back-stripes{position:absolute;left:0;top:0;width:100%;height:100%}
</style>
</head>
<body>

<section class="card card-front">
  <div class="brand">VELMIRA</div>

  <div class="person">
    <div class="person-name">NOME | SOBRENOME</div>
    <div class="person-role">CARGO</div>
  </div>

  <ul class="contacts">
    <li class="phones">(61) 3274.5810 | (61) 3274.5810</li>
    <li>
      <span class="icon">
        <svg width="18" height="14" viewBox="0 0 18 14"><rect x="1" y="1" width="16" height="12" fill="none" stroke="#0f4a68" stroke-width="2"/><path d="M1 1l8 7 8-7" fill="none" stroke="#0f4a68" stroke-width="2"/></svg>
      </span>contato@velmira.com.br
    </li>
    <li><span class="icon"></span>/velmira</li>
    <li><span class="icon"></span>@velmira</li>
  </ul>

  <div class="address">
    <div class="address-label">Endereço:</div>
    <div>Av. das Palmeiras, 2480 | Centro | Cidade/UF</div>
    <div>Cep: 70352-140</div>
  </div>
  <div class="address-bar"></div>

  <svg class="front-bands" viewBox="0 0 960 80" preserveAspectRatio="none">
    <rect x="0" y="30" width="960" height="50" fill="#1a6d92"/>
    <rect x="0" y="42" width="960" height="38" fill="#3d9fc4"/>
    <rect x="0" y="58" width="960" height="22" fill="#7cc4de"/>
    <polygon points="620,42 960,42 960,20 650,20" fill="#3d9fc4"/>
  </svg>
</section>

<section class="card card-back">
  <svg class="back-stripes" viewBox="0 0 960 533" preserveAspectRatio="none">
    <polygon points="40,0 70,0 70,533 40,533" fill="#0f4a68"/>
    <polygon points="90,0 104,0 104,533 90,533" fill="#1a6d92"/>
    <polygon points="122,0 130,0 130,533 122,533" fill="#3d9fc4"/>
  </svg>
</section>

</body>
</html>
```